Halvorn Minerals Web Design

Require a Web page design for an international mining and private investment company currently based in Dubai, UAE. I would like to view designs that incorporate our current corporate logo design aimed at communicating global business development/expansion across a diversity of commodities within the mining and investment sectors.

We are a global organisation with global experience and strategy with specific business development focus in Africa, Central and South America.

Target Market(s)

Mining industry, finance, fund raising, brokering, private equity and public stock exchanges.

Industry/Entity Type

Mining

Number of Pages Required

5+ page

Font styles to use
Sans Serif

Colors

Designer to choose colors to be used in the design.

Requirements
Must have
• Corporate logo, description of who we are, what we do, corporate mission, vision & strategy.
Nice to have
• Inclusion of images, photos, interactive maps/graphics and video.

```html
<!DOCTYPE html>
<html lang="en">
<head>
<meta charset="utf-8">
<title>Halvorn Minerals</title>
<link href="https://fonts.googleapis.com/css2?family=Montserrat:wght@400;600;700&family=Open+Sans:wght@400;600&family=Oswald:wght@500;700&display=swap" rel="stylesheet">
<style>
:root{
  --gold:#c9a24a;
  --gold-dark:#a8832f;
  --ink:#1b1916;
  --ink-deep:#121110;
  --ink-soft:#26231f;
  --paper:#ecebe8;
  --paper-card:#ffffff;
  --text-light:#c9c4ba;
  --text-mute:#8f8a80;
  --text-dark:#3a3631;
}
*{box-sizing:border-box;margin:0;padding:0}
html,body{width:1200px;height:2948px;overflow:hidden}
body{font-family:"Open Sans",Arial,sans-serif;color:var(--text-light);background:var(--ink);font-size:12px;line-height:1.6}
h1,h2,h3,h4{font-family:"Montserrat",Arial,sans-serif;font-weight:700}
.page{position:relative;width:1200px;height:2948px}

/* header */
.site-header{position:absolute;top:0;left:0;width:1200px;height:88px;background:var(--ink-deep);z-index:2}
.brand{position:absolute;left:118px;top:12px;display:flex;align-items:center;gap:10px}
.brand-mark{width:34px;height:34px;background:var(--gold)}
.brand-name{font-family:"Montserrat",Arial,sans-serif;font-weight:700;font-size:17px;color:var(--gold);letter-spacing:.5px}
.header-contact{position:absolute;right:118px;top:14px;display:flex;gap:10px;align-items:center;color:var(--text-light);font-size:11px;line-height:1.4}
.header-contact .icon{width:28px;height:28px;border-radius:50%;background:var(--gold);display:flex;align-items:center;justify-content:center}
.main-nav{position:absolute;left:118px;right:118px;top:60px;height:24px;display:flex;border-top:1px solid #3a352d}
.main-nav a{flex:1;text-align:center;font-family:"Montserrat",Arial,sans-serif;font-size:10px;font-weight:600;text-transform:uppercase;color:var(--text-light);text-decoration:none;line-height:24px;letter-spacing:.5px}
.main-nav a.active{background:var(--gold);color:var(--ink-deep)}

/* hero */
.hero{position:absolute;top:88px;left:0;width:1200px;height:392px;background:linear-gradient(100deg,#1a1611 0%,#3b2f20 45%,#6b5333 70%,#2a2117 100%)}
.hero-copy{position:absolute;left:118px;top:120px;width:470px}
.hero-copy h1{font-size:25px;line-height:1.3;color:#fff}
.btn{display:inline-block;background:var(--gold);color:var(--ink-deep);font-family:"Montserrat",Arial,sans-serif;font-size:10px;font-weight:700;text-transform:uppercase;padding:7px 16px;margin-top:22px}
.hero-dots{position:absolute;left:0;right:0;bottom:18px;display:flex;justify-content:center;gap:6px}
.hero-dots span{width:8px;height:8px;border-radius:50%;background:#6d6558}
.hero-dots span.on{background:var(--gold)}

/* quick links */
.quick-links{position:absolute;top:480px;left:0;width:1200px;height:420px;background:var(--paper)}
.quick-links .cards{position:absolute;left:300px;top:168px;display:flex;gap:18px}
.quick-card{width:186px;text-align:center}
.quick-card .photo{height:160px}
.quick-card p{font-family:"Montserrat",Arial,sans-serif;font-weight:600;color:var(--text-dark);font-size:13px;margin-top:14px}

/* who we are */
.who{position:absolute;top:900px;left:0;width:1200px;height:480px;background:var(--ink)}
.who-photo{position:absolute;left:222px;top:50px;width:360px;height:212px;border:2px solid var(--gold);background:linear-gradient(135deg,#2b241b,#5a4630 60%,#2a2118)}
.who-copy{position:absolute;left:620px;top:50px;width:380px}
.who-copy h2{color:#fff;font-size:22px}
.who-copy .lead{color:var(--gold);font-weight:600;font-size:12px;margin:4px 0 14px}
.who-copy p{font-size:11px;color:var(--text-mute)}
.who-copy .more{color:var(--gold);font-size:10px;font-weight:600;text-transform:uppercase;margin-top:10px}
.pillars{position:absolute;left:222px;top:320px;display:flex;gap:56px}
.pillar{width:220px;display:flex;gap:12px}
.pillar svg{flex:none}
.pillar h3{font-size:13px;color:#fff;margin-bottom:4px}
.pillar p{font-size:10.5px;color:var(--text-mute);line-height:1.5}

/* project experience */
.projects{position:absolute;top:1380px;left:0;width:1200px;height:420px;background:var(--paper)}
.projects-photo{position:absolute;left:0;top:0;width:600px;height:420px;background:linear-gradient(160deg,#c98c4c 0%,#a66f3c 40%,#6e4a2c 75%,#3a2a1d 100%)}
.projects-title{position:absolute;left:380px;top:150px;text-align:center}
.projects-title h2{font-family:"Oswald",Arial,sans-serif;font-weight:700;font-size:40px;line-height:1.05;color:#fff;text-transform:uppercase}
.projects-title .btn{margin-top:12px}
.projects-copy{position:absolute;left:648px;top:40px;width:420px;color:var(--text-dark);font-size:11px}
.projects-copy p{margin-bottom:14px}
.projects-copy strong{color:var(--gold-dark)}

/* team */
.team{position:absolute;top:1800px;left:0;width:1200px;height:460px;background:var(--ink)}
.team-bar{position:absolute;left:168px;top:50px;width:72px;height:330px;background:var(--gold)}
.team-list{position:absolute;left:262px;top:66px;display:flex;flex-direction:column;gap:26px}
.avatar{width:54px;height:54px;border-radius:50%;border:2px solid var(--gold);background:linear-gradient(160deg,#6d655a,#3a352f)}
.team-copy{position:absolute;left:380px;top:40px;width:640px}
.team-copy h2{color:#fff;font-size:20px;margin-bottom:18px}
.team-copy p{font-size:11px;color:var(--text-mute)}
.team-copy .name{color:var(--gold);font-family:"Montserrat",Arial,sans-serif;font-weight:600;font-size:13px;margin-top:50px}
.team-copy .role{font-size:11px;color:var(--text-light)}

/* blog + testimonials */
.news{position:absolute;top:2260px;left:0;width:1200px;height:380px;background:var(--paper);color:var(--text-dark)}
.news h2{font-size:20px;color:var(--ink)}
.blog{position:absolute;left:118px;top:30px;width:440px}
.post{display:flex;gap:14px;margin-top:16px}
.post .thumb{width:92px;height:64px;flex:none}
.post h4{font-size:11px;color:var(--ink)}
.post .meta{font-size:9px;color:var(--gold-dark)}
.post p{font-size:10px;line-height:1.45}
.testimonials{position:absolute;left:640px;top:30px;width:440px}
.quote-box{margin-top:18px;background:var(--paper-card);padding:22px 24px 22px 60px;position:relative;font-size:11px}
.quote-box .mark{position:absolute;left:20px;top:14px;font-family:"Montserrat",Arial,sans-serif;font-size:40px;color:var(--gold);line-height:1}
.quote-box .author{margin-top:12px;font-weight:600;color:var(--ink)}
.quote-box .author span{display:block;font-weight:400;font-size:10px;color:var(--text-mute)}

/* footer */
.site-footer{position:absolute;top:2640px;left:0;width:1200px;height:308px;background:var(--ink-deep)}
.footer-band{height:56px;background:linear-gradient(180deg,#3a342b,#1b1814)}
.footer-nav{position:absolute;top:62px;left:300px;right:300px;display:flex;justify-content:space-between;font-size:9.5px;color:var(--text-mute)}
.footer-cols{position:absolute;left:118px;top:100px;display:flex;gap:56px;font-size:10.5px;color:var(--text-mute);line-height:1.5}
.footer-cols h4{color:#fff;font-size:12px;margin-bottom:6px}
.footer-cols .line{display:flex;gap:8px;align-items:center;margin-bottom:6px}
.dot-icon{width:18px;height:18px;border-radius:50%;background:var(--gold);flex:none}
.newsletter input{display:block;width:200px;height:26px;border:none;background:#fff;margin:4px 0 8px;font-size:10px;padding:0 8px}
.newsletter .btn{margin-top:0;padding:5px 18px}
.footer-bottom{position:absolute;left:0;right:0;bottom:0;height:44px;border-top:1px solid #2c2822;display:flex;align-items:center;justify-content:space-between;padding:0 118px;font-size:9.5px;color:var(--text-mute)}
.social{display:flex;gap:6px}
.social span{width:20px;height:20px;background:#3a352e}
</style>
</head>
<body>
<div class="page">

<header class="site-header">
  <div class="brand"><span class="brand-mark"></span><span class="brand-name">Halvorn Minerals</span></div>
  <div class="header-contact">
    <span class="icon"><svg width="14" height="14" viewBox="0 0 24 24"><path d="M6.6 10.8a15 15 0 006.6 6.6l2.2-2.2c.3-.3.7-.4 1-.2 1.1.4 2.3.6 3.6.6.6 0 1 .4 1 1V20c0 .6-.4 1-1 1A17 17 0 013 4c0-.6.4-1 1-1h3.5c.6 0 1 .4 1 1 0 1.3.2 2.5.6 3.6.1.3 0 .7-.2 1z" fill="#121110"/></svg></span>
    <div>Have a question? Call us today<br><strong>+971 4 555 0134</strong></div>
  </div>
  <nav class="main-nav">
    <a class="active">Executive Summary</a><a>Team &amp; Experience</a><a>Commercial</a><a>Business Model</a><a>Projects</a><a>Contact</a>
  </nav>
</header>

<section class="hero">
  <div role="img" aria-label="Miners in hard hats working underground" style="position:absolute;inset:0"></div>
  <div class="hero-copy">
    <h1>A platform for execution of global mining projects with an initial focus on South America, Central America &amp; Africa.</h1>
    <span class="btn">Get Started</span>
  </div>
  <div class="hero-dots"><span class="on"></span><span></span><span></span></div>
</section>

<section class="quick-links">
  <div class="cards">
    <div class="quick-card"><div class="photo" role="img" aria-label="Hands holding a small plant" style="background:linear-gradient(135deg,#4a5b3a,#8a9a6a)"></div><p>Social Responsibility</p></div>
    <div class="quick-card"><div class="photo" role="img" aria-label="Investors meeting at a table" style="background:linear-gradient(135deg,#6f86a3,#c7d3df)"></div><p>Investors</p></div>
    <div class="quick-card"><div class="photo" role="img" aria-label="Business team shaking hands" style="background:linear-gradient(135deg,#4d6d96,#a9bcd4)"></div><p>Contact Us</p></div>
  </div>
</section>

<section class="who">
  <div class="who-photo" role="img" aria-label="Miners with helmet lamps in a tunnel"></div>
  <div class="who-copy">
    <h2>Who We Are</h2>
    <div class="lead">Mining industry connections &amp; networks in Africa, South America &amp; Central America</div>
    <p>Halvorn Minerals brings together seasoned operators and investors to develop mineral assets across emerging regions. Our team combines technical mining expertise with access to private equity, public markets and strategic partners, allowing us to move projects from discovery to production with discipline and care for local communities.</p>
    <div class="more">Learn more about us →</div>
  </div>
  <div class="pillars">
    <div class="pillar"><svg width="30" height="30" viewBox="0 0 30 30"><circle cx="15" cy="15" r="12" fill="none" stroke="#c9a24a" stroke-width="2"/><circle cx="15" cy="15" r="5" fill="#c9a24a"/></svg><div><h3>Our Mission</h3><p>Deliver responsible mining projects that create lasting value for partners and regions.</p></div></div>
    <div class="pillar"><svg width="30" height="30" viewBox="0 0 30 30"><path d="M2 15c4-7 9-10 13-10s9 3 13 10c-4 7-9 10-13 10S6 22 2 15z" fill="none" stroke="#c9a24a" stroke-width="2"/><circle cx="15" cy="15" r="4" fill="#c9a24a"/></svg><div><h3>Our Vision</h3><p>Become a trusted global platform for mineral development and investment.</p></div></div>
    <div class="pillar"><svg width="30" height="30" viewBox="0 0 30 30"><path d="M4 26V14M12 26V8M20 26V16M28 26V4" stroke="#c9a24a" stroke-width="3"/></svg><div><h3>Our Strategy</h3><p>Focus on diverse commodities with clear paths to funding and production.</p></div></div>
  </div>
</section>

<section class="projects">
  <div class="projects-photo" role="img" aria-label="Engineer overlooking an open-pit mine at sunset"></div>
  <div class="projects-title"><h2>Project<br>Experience</h2><span class="btn">View Our Projects</span></div>
  <div class="projects-copy">
    <p>Combined experience of <strong>Brazil, Burkina Faso, Cote d'Ivoire, Colombia, Mali, Peru, Ghana and Tanzania</strong> with work across gold, copper, iron ore and base metal projects at every stage of development.</p>
    <p><strong>Exploration</strong> – Our team has guided early stage programs from first sampling through resource definition, building geological models that support confident investment decisions for partners.</p>
    <p><strong>Development</strong> – We have delivered feasibility studies, permitting and construction for mines of varied scale, coordinating engineering, finance and community engagement.</p>
    <p><strong>Operations</strong> – Our operators bring decades of site leadership, improving safety, recovery and cost performance across open pit and underground mines.</p>
  </div>
</section>

<section class="team">
  <div class="team-bar"></div>
  <div class="team-list">
    <div class="avatar" role="img" aria-label="Portrait of team member"></div>
    <div class="avatar" role="img" aria-label="Portrait of team member"></div>
    <div class="avatar" role="img" aria-label="Portrait of team member"></div>
    <div class="avatar" role="img" aria-label="Portrait of team member"></div>
  </div>
  <div class="team-copy">
    <h2>Executive Team</h2>
    <p>Over 25 years of experience in exploration, mine development, corporate finance and operations across four continents. He has led teams that raised capital for several listed resource companies, negotiated joint ventures with national governments and oversaw the construction of producing gold and copper mines. His background spans geology, project management and strategic planning, with a strong focus on safety, transparency and long term relationships with host communities. He holds advanced degrees in mining engineering and business, and is a fellow of several professional institutes supporting the next generation of mining leaders.</p>
    <div class="name">Marcus Ellery</div>
    <div class="role">CEO</div>
  </div>
</section>

<section class="news">
  <div class="blog">
    <h2>From the Blog</h2>
    <div class="post"><div class="thumb" role="img" aria-label="Mining trucks on a haul road" style="background:linear-gradient(135deg,#8a6a45,#c9a072)"></div><div><h4>Lorem ipsum dolor sit amet</h4><div class="meta">March 12 · 3 Comments</div><p>Notes on new copper finds and what they mean for regional investors this year.</p></div></div>
    <div class="post"><div class="thumb" role="img" aria-label="Drilling rig at a mine site" style="background:linear-gradient(135deg,#5e5448,#a69680)"></div><div><h4>Lorem ipsum dolor sit amet</h4><div class="meta">March 04 · 2 Comments</div><p>A short review of drilling results from our latest West African program.</p></div></div>
    <div class="post"><div class="thumb" role="img" aria-label="Excavator loading ore" style="background:linear-gradient(135deg,#a07a3c,#d6b57a)"></div><div><h4>Lorem ipsum dolor sit amet</h4><div class="meta">February 21 · 5 Comments</div><p>How disciplined funding keeps mine development on time and on budget.</p></div></div>
  </div>
  <div class="testimonials">
    <h2>Testimonials</h2>
    <div class="quote-box">
      <span class="mark">“</span>
      Working with the Halvorn Minerals team gave us clear insight into every stage of the project. Their guidance on funding and local partnerships helped us move forward with confidence, and their reporting was always open and timely. We look forward to growing together across new regions in the coming years.
      <div class="author">– Daniel Okafor<span>Investment Partner</span></div>
    </div>
  </div>
</section>

<footer class="site-footer">
  <div class="footer-band" role="img" aria-label="Silhouette of mining machinery and workers"></div>
  <div class="footer-nav"><span>Executive Summary</span><span>Team &amp; Experience</span><span>Commercial</span><span>Business Model</span><span>Projects</span><span>Contact</span></div>
  <div class="footer-cols">
    <div><h4>Dubai, UAE</h4>Office 1402, Harbour Tower<br>Business Bay District<br>PO Box 55012<br>Dubai, UAE</div>
    <div><h4>Tessaly, West Africa</h4>Suite 7, Riverside Plaza<br>Central Avenue<br>PO Box 318<br>Tessaly</div>
    <div>
      <div class="line"><span class="dot-icon"></span>+971 4 555 0134<br>+971 4 555 0135</div>
      <div class="line"><span class="dot-icon"></span>Tower Road, Business Bay</div>
      <div class="line"><span class="dot-icon"></span>info@halvornminerals.com</div>
    </div>
    <div class="newsletter"><h4>Subscribe Newsletter</h4><input type="text" placeholder="Your email address"><span class="btn">Subscribe</span></div>
  </div>
  <div class="footer-bottom"><span>© 2024 Halvorn Minerals. All Rights Reserved.</span><div class="social"><span></span><span></span><span></span></div></div>
</footer>

</div>
</body>
</html>
```